Design Business Cards, letterhead and logo for new setup company

Please help us to design for name card, letterhead and envelope.

For colour -

Card background: grey
logo: gold
words: red, blue OR orange

Any shade of the above colours are fine, from light to dark, the designer can choose as they wish

Logo design: see attached
Namecard layout: see attached

Corporate identity should include:

a) logo design

b) namecard design

c) letterhead design

d) envelope design

we will want the designer to eventually give us a working file of the image so that we can
1) change names/ do any amendments on our own easily
2) in a format/ program which most people/ printing companies have
3) in a big enough resolution so that the printing will be clear and sharp
4) specifically for letterhead and envelope design, it should also be provided in a format compatible with MS word so that we can use it for our documents

```html
<!DOCTYPE html>
<html lang="en">
<head>
<meta charset="utf-8">
<title>Northvale Medical Supplies – Business Card</title>
<link rel="stylesheet" href="https://fonts.googleapis.com/css2?family=Open+Sans:wght@400;600;700&display=swap">
<style>
  :root {
    --page: #dcd9d0;
    --card: #4a4b4d;
    --card-dark: #3f4042;
    --gold: #d4a935;
    --accent: #e2613a;
    --rule: #d8c62a;
    --text: #f2f2f2;
    --muted: #cfcfcf;
  }
  html, body {
    margin: 0;
    width: 1200px;
    height: 800px;
    overflow: hidden;
    background: var(--page);
  }
  .business-card {
    position: absolute;
    left: 75px;
    top: 100px;
    width: 1050px;
    height: 600px;
    box-shadow: 0 10px 30px rgba(0,0,0,0.25);
  }
  .business-card svg { display: block; }
  .type { font-family: "Open Sans", Arial, sans-serif; }
</style>
</head>
<body>
<div class="business-card">
  <svg width="1050" height="600" viewBox="0 0 1050 600" xmlns="http://www.w3.org/2000/svg" class="type">
    <!-- card face -->
    <rect class="card-face" x="0" y="0" width="1050" height="600" fill="var(--card)"/>

    <!-- company name block -->
    <g class="company-mark">
      <rect x="62" y="98" width="46" height="46" fill="var(--gold)"/>
      <text x="124" y="122" font-size="30" font-weight="700" fill="var(--gold)">NORTHVALE MEDICAL</text>
      <text x="126" y="148" font-size="19" font-weight="700" fill="var(--gold)" letter-spacing="2">Supplies Pte Ltd</text>
    </g>

    <!-- person -->
    <g class="person">
      <text x="985" y="98" text-anchor="end" font-size="38" font-weight="700" fill="var(--accent)">Marcus Hale</text>
      <text x="985" y="130" text-anchor="end" font-size="22" fill="var(--muted)">Managing Director</text>
    </g>

    <!-- rules -->
    <line class="rule-top" x1="560" y1="146" x2="995" y2="146" stroke="var(--rule)" stroke-width="3"/>
    <line class="rule-mid" x1="60" y1="268" x2="530" y2="268" stroke="var(--rule)" stroke-width="3"/>

    <!-- icon tab -->
    <path class="icon-tab" d="M0 285 H72 Q90 285 90 303 V502 Q90 520 72 520 H0 Z" fill="var(--accent)"/>
    <g class="contact-icons" fill="#ffffff">
      <!-- phone -->
      <path d="M36 296 q-6 4 -2 12 q4 8 12 10 q6 1 8 -4 l-5 -4 l-3 3 q-5 -2 -7 -7 l3 -3 z"/>
      <!-- mobile -->
      <rect x="38" y="330" width="12" height="20" rx="2"/>
      <!-- fax -->
      <rect x="35" y="372" width="18" height="12" rx="2"/>
      <rect x="39" y="364" width="10" height="8"/>
      <!-- email -->
      <rect x="33" y="404" width="22" height="15" rx="2"/>
      <!-- web -->
      <circle cx="44" cy="448" r="10"/>
      <!-- home -->
      <path d="M33 487 L44 476 L55 487 H52 V498 H36 V487 Z"/>
    </g>

    <!-- contact details -->
    <g class="contact-lines" font-size="22" fill="var(--text)">
      <text x="140" y="312">+9907745132</text>
      <text x="140" y="347">+9907745132</text>
      <text x="140" y="382">+9907745132</text>
      <text x="140" y="417">contact@northvalemed.com</text>
      <text x="140" y="452">www.northvalemed.com</text>
      <text x="140" y="494">1480 Larkspur Ave. Fairmont, TX 75210</text>
    </g>

    <!-- bottom band -->
    <path class="band-shadow" d="M0 550 H560 C592 550 598 510 632 510 H1050 V522 H640 C608 522 600 562 566 562 H0 Z" fill="var(--card-dark)"/>
    <path class="bottom-band" d="M0 562 H566 C600 562 608 522 640 522 H1050 V600 H0 Z" fill="var(--accent)"/>
  </svg>
</div>
</body>
</html>
```